Business Card Design

Attached is the logo of the store.

Information needed on the business card:

www.brookvale17vino.com
info@brookvale17vino.com
412 Harlow St NY, NY 10027
Tel:(646) 472-3958

Store Hours
Mon-Sat Noon-10pm
Sun Noon-8pm

Free Deliveries

Industry/Entity Type

Business

Contact Information for Business Card

Brookvale 17 Wine & Spirits

```html
<!DOCTYPE html>
<html lang="en">
<head>
<meta charset="utf-8">
<title>Brookvale 17 Wine &amp; Spirits – Business Card</title>
<link rel="stylesheet" href="https://fonts.googleapis.com/css2?family=Questrial&family=Cormorant+Garamond:ital,wght@1,600&display=swap">
<style>
  :root {
    --stage: #d9d9d9;
    --ink-black: #0b0b0b;
    --wine: #3a1416;
    --wine-deep: #2c0e10;
    --gold: #e4dca0;
    --cream: #f1efc4;
    --text-cream: #ece6b4;
    --name-light: #f3ecec;
  }
  * { box-sizing: border-box; margin: 0; padding: 0; }
  html, body { width: 1200px; height: 900px; overflow: hidden; }
  body {
    background: var(--stage);
    font-family: "Questrial", "Century Gothic", sans-serif;
    position: relative;
  }
  .card {
    position: absolute;
    width: 700px;
    height: 400px;
    left: 250px;
    overflow: hidden;
    box-shadow: 0 6px 18px rgba(0,0,0,.25);
  }

  /* Back side: contact details */
  .card-back { top: 40px; background: var(--ink-black); }
  .card-back .hours-band {
    position: absolute; left: 0; right: 0; bottom: 0; height: 82px;
    background: var(--wine);
    border-top: 4px solid var(--gold);
    color: var(--text-cream);
    font-size: 25px; letter-spacing: 1px;
    display: flex; align-items: center; justify-content: center; gap: 12px;
  }
  .card-back .brand-mark {
    position: absolute; top: 26px; right: 34px;
    font-size: 22px; color: #5a3335; letter-spacing: 1px;
  }
  .card-back .address {
    position: absolute; top: 108px; left: 40px;
    color: var(--text-cream); font-size: 19px; line-height: 33px;
    letter-spacing: 1px; text-align: right;
  }
  .card-back .divider {
    position: absolute; left: 374px; top: 70px; width: 1px; height: 200px;
    background: linear-gradient(var(--gold), rgba(228,220,160,0));
    opacity: .7;
  }
  .card-back .contacts {
    position: absolute; top: 94px; left: 400px; list-style: none;
    color: var(--text-cream); font-size: 17px; letter-spacing: 1px;
  }
  .card-back .contacts li { display: flex; align-items: center; gap: 12px; height: 32px; }
  .card-back .contacts svg { width: 22px; height: 22px; }
  .card-back .tagline {
    position: absolute; right: 34px; bottom: 110px;
    font-family: "Cormorant Garamond", Georgia, serif; font-style: italic; font-weight: 600;
    font-size: 24px; letter-spacing: 2px; color: var(--text-cream);
  }

  /* Front side: name */
  .card-front { top: 470px; background: linear-gradient(160deg, var(--wine) 0%, var(--wine-deep) 100%); }
  .card-front .brand-name {
    position: absolute; top: 96px; left: 0; right: 0; text-align: center;
    font-size: 72px; color: var(--name-light); letter-spacing: 3px;
  }
  .card-front .web-band {
    position: absolute; left: 0; right: 0; top: 236px; height: 56px;
    background: var(--cream);
    display: flex; align-items: center; justify-content: center;
    font-size: 32px; letter-spacing: 3px; color: var(--wine-deep);
  }
</style>
</head>
<body>

<section class="card card-back" aria-label="Card back">
  <div class="brand-mark">Brookvale 17</div>

  <address class="address" style="font-style:normal">
    Brookvale 17 Wine &amp; Spirits<br>
    412 Harlow Street<br>
    New York, NY 10027
  </address>

  <div class="divider"></div>

  <ul class="contacts">
    <li>
      <svg viewBox="0 0 22 22" aria-hidden="true"><circle cx="11" cy="11" r="10" fill="none" stroke="#ece6b4" stroke-width="1.5"/><path d="M7.5 6.5c0 5 3 8 8 8l1-2-2.5-1-1 1c-1.5-.7-2.8-2-3.5-3.5l1-1-1-2.5z" fill="#ece6b4"/></svg>
      (646) 472-3958
    </li>
    <li>
      <svg viewBox="0 0 22 22" aria-hidden="true"><circle cx="11" cy="11" r="10" fill="none" stroke="#ece6b4" stroke-width="1.5"/><rect x="6" y="7.5" width="10" height="7" fill="none" stroke="#ece6b4" stroke-width="1.3"/><path d="M6 7.5l5 4 5-4" fill="none" stroke="#ece6b4" stroke-width="1.3"/></svg>
      info@brookvale17vino.com
    </li>
    <li>
      <svg viewBox="0 0 22 22" aria-hidden="true"><circle cx="11" cy="11" r="10" fill="none" stroke="#ece6b4" stroke-width="1.5"/><circle cx="11" cy="11" r="6" fill="none" stroke="#ece6b4" stroke-width="1.2"/><ellipse cx="11" cy="11" rx="2.6" ry="6" fill="none" stroke="#ece6b4" stroke-width="1.2"/><path d="M5 11h12" stroke="#ece6b4" stroke-width="1.2"/></svg>
      www.brookvale17vino.com
    </li>
  </ul>

  <p class="tagline">Free Deliveries</p>

  <div class="hours-band">
    <span>Store Hours</span><span>•</span><span>Mon-Sat Noon-10pm</span><span>•</span><span>Sun Noon-8pm</span>
  </div>
</section>

<section class="card card-front" aria-label="Card front">
  <h1 class="brand-name" style="font-weight:400">Brookvale 17</h1>
  <div class="web-band">www.brookvale17vino.com</div>
</section>

</body>
</html>
```